Banner Project for website

We do not like our current banner and need this updated. Our website is:
https://inkvelby.com/
We need the banner to have the following wording on the left side:
See attachment. (screenshot text on the left)
On the right side, I want to replace the lady and have a nice image of printed products like the following websites which have an image with different printed prodcuts bundled together or seperately.
https://www.glavorpatch.com/
https://boxtrundo.com/
The banner must look fresh and vibrant
Target Market(s)
Small businesses
Industry/Entity Type
Printing
Requirements
Must have
- Greta banner image

```html
<!DOCTYPE html>
<html lang="en">
<head>
<meta charset="utf-8">
<title>Inkvelby – Compare Quotes &amp; Save</title>
<link rel="stylesheet" href="https://fonts.googleapis.com/css2?family=Open+Sans:wght@300;400;600;700;800&family=Montserrat:wght@600;700&display=swap">
<style>
  :root{
    --brand-blue:#0d5c9c;
    --brand-blue-light:#1a6fb2;
    --brand-yellow:#fcc536;
    --ink:#2b2b2b;
    --muted:#6b6b6b;
    --line:#e4e4e4;
    --white:#ffffff;
    --card-red:#d8261b;
    --card-yellow:#f2c21a;
    --card-orange:#f35a2b;
    --card-blue:#2a73c4;
  }
  *{margin:0;padding:0;box-sizing:border-box}
  html,body{width:1200px;height:675px;overflow:hidden;background:var(--white);font-family:"Open Sans",sans-serif;color:var(--ink)}
  .page{position:relative;width:1200px;height:675px}

  .site-header{height:60px;background:#f6f6f6;display:flex;align-items:center;padding-left:209px;gap:40px}
  .brand{display:flex;flex-direction:column;line-height:1}
  .brand-name{font-family:"Montserrat",sans-serif;font-weight:700;font-size:17px;letter-spacing:2px;color:#666}
  .brand-tag{font-size:9px;color:#888;margin-top:4px;letter-spacing:.5px}
  .header-search{width:283px;height:26px;border:1px solid #c9d6e3;background:var(--white);border-radius:2px}

  .main-nav{height:38px;border-bottom:1px solid var(--line);display:flex;align-items:center;padding-left:209px;gap:19px}
  .nav-item{font-family:"Montserrat",sans-serif;font-weight:700;font-size:8.2px;letter-spacing:.2px;color:#333;display:flex;align-items:center;gap:5px}
  .nav-item svg{width:7px;height:5px}

  .hero{position:relative;height:306px;background:var(--brand-blue);overflow:hidden}
  .hero-stripes{position:absolute;inset:0}
  .hero-title{position:absolute;left:190px;top:28px;font-weight:800;font-size:36px;line-height:33px;color:var(--brand-yellow);letter-spacing:-.3px}
  .hero-copy{position:absolute;left:188px;top:114px;width:260px;color:var(--white);font-size:13.4px;line-height:16.5px}
  .hero-copy p+p{margin-top:16px}
  .quote-form{position:absolute;left:188px;top:198px;width:237px;display:flex;flex-direction:column;gap:7px}
  .quote-field{height:19px;background:var(--white)}
  .quote-button{height:19px;background:var(--brand-yellow)}

  .steps{position:absolute;left:568px;top:40px;display:flex;align-items:center;gap:12px;color:var(--white);font-size:17px}
  .step{display:flex;align-items:center;gap:7px}
  .step svg{display:block}
  .step strong{font-weight:700}

  .hero-visual{position:absolute;left:478px;top:80px;width:578px;height:212px;
    background:linear-gradient(120deg,#1f3f5a 0%,#3f8fd0 30%,#f07a3a 45%,#e9d7c9 62%,#8fc2e6 75%,#dcdfe6 100%);
    border-radius:6px 40px 6px 6px;opacity:.92}

  .categories{padding-top:22px;text-align:center}
  .categories-title{font-weight:300;font-size:17px;color:#555;letter-spacing:.3px}
  .category-grid{display:flex;gap:10px;justify-content:center;margin-top:30px}
  .category-card{position:relative;width:185px;height:198px;text-align:left;overflow:hidden}
  .category-card h3{position:absolute;left:22px;top:22px;font-family:"Montserrat",sans-serif;font-weight:700;font-size:13.5px;line-height:15px;color:var(--white);text-transform:uppercase}
  .card-banner{background:linear-gradient(135deg,#e5301f,#b5160e)}
  .card-brochures{background:linear-gradient(135deg,#f5c61a,#e8b00f)}
  .card-business{background:linear-gradient(135deg,#f76632,#e8481f)}
  .card-labels{background:linear-gradient(135deg,#3a84d2,#1f5ea8)}
</style>
</head>
<body>
<div class="page">
  <header class="site-header">
    <div class="brand">
      <span class="brand-name">INKVELBY</span>
      <span class="brand-tag">Printing Marketplace</span>
    </div>
    <div class="header-search"></div>
  </header>

  <nav class="main-nav">
    <span class="nav-item">BANNERS &amp; SIGNS <svg viewBox="0 0 7 5"><path d="M.5 .8 3.5 4 6.5 .8" fill="none" stroke="#333" stroke-width="1"/></svg></span>
    <span class="nav-item">BUSINESS CARDS <svg viewBox="0 0 7 5"><path d="M.5 .8 3.5 4 6.5 .8" fill="none" stroke="#333" stroke-width="1"/></svg></span>
    <span class="nav-item">BROCHURES &amp; FLYERS <svg viewBox="0 0 7 5"><path d="M.5 .8 3.5 4 6.5 .8" fill="none" stroke="#333" stroke-width="1"/></svg></span>
    <span class="nav-item">DECALS <svg viewBox="0 0 7 5"><path d="M.5 .8 3.5 4 6.5 .8" fill="none" stroke="#333" stroke-width="1"/></svg></span>
    <span class="nav-item">LABELS &amp; STICKERS <svg viewBox="0 0 7 5"><path d="M.5 .8 3.5 4 6.5 .8" fill="none" stroke="#333" stroke-width="1"/></svg></span>
    <span class="nav-item">MAGNETS <svg viewBox="0 0 7 5"><path d="M.5 .8 3.5 4 6.5 .8" fill="none" stroke="#333" stroke-width="1"/></svg></span>
    <span class="nav-item">MARKETING MATERIALS <svg viewBox="0 0 7 5"><path d="M.5 .8 3.5 4 6.5 .8" fill="none" stroke="#333" stroke-width="1"/></svg></span>
  </nav>

  <section class="hero">
    <svg class="hero-stripes" width="1200" height="306" viewBox="0 0 1200 306">
      <polygon points="0,60 120,306 70,306 0,160" fill="#125f9f"/>
      <polygon points="0,0 60,0 260,306 200,306 0,40" fill="#0b5492" opacity=".6"/>
      <polygon points="120,0 150,0 360,306 330,306" fill="#1565a6" opacity=".5"/>
    </svg>

    <h1 class="hero-title">Compare Quotes<br>&amp; Save</h1>
    <div class="hero-copy">
      <p>Get instant quotes, compare products from multiple printers and get the best price.</p>
      <p>Easy online ordering and free deisgn.</p>
    </div>
    <div class="quote-form">
      <div class="quote-field"></div>
      <div class="quote-field"></div>
      <div class="quote-button"></div>
    </div>

    <div class="steps">
      <div class="step">
        <svg width="25" height="25" viewBox="0 0 25 25"><circle cx="10" cy="10" r="8" fill="none" stroke="#fff" stroke-width="1.6"/><circle cx="10" cy="10" r="5" fill="none" stroke="#fff" stroke-width="1"/><path d="M16 16 23 23" stroke="#fff" stroke-width="2.4" stroke-linecap="round"/></svg>
        <span>Search</span>
      </div>
      <svg width="13" height="12" viewBox="0 0 13 12"><path d="M1 4h5V1l6 5-6 5V8H1z" fill="none" stroke="#fff" stroke-width="1.1"/></svg>
      <div class="step">
        <svg width="28" height="28" viewBox="0 0 28 28"><rect x="2" y="2" width="24" height="17" fill="none" stroke="#fff" stroke-width="1.3"/><path d="M5 6h7M5 9h7M16 6h7M16 9h7M5 12h7M16 12h7" stroke="#fff" stroke-width="1"/><circle cx="14" cy="19" r="4" fill="var(--brand-blue)" stroke="#fff" stroke-width="1.3"/><path d="M14 23v4" stroke="#fff" stroke-width="1.3"/></svg>
        <span>Compare</span>
      </div>
      <svg width="13" height="12" viewBox="0 0 13 12"><path d="M1 4h5V1l6 5-6 5V8H1z" fill="none" stroke="#fff" stroke-width="1.1"/></svg>
      <div class="step">
        <svg width="29" height="27" viewBox="0 0 29 27"><rect x="2" y="2" width="16" height="11" fill="none" stroke="#fff" stroke-width="1.3"/><rect x="9" y="9" width="18" height="16" fill="var(--brand-blue)" stroke="#fff" stroke-width="1.3"/><path d="M11 22l5-6 4 4 3-3 3 5" fill="none" stroke="#fff" stroke-width="1.1"/><circle cx="14" cy="13" r="1.5" fill="#fff"/></svg>
        <span>Ink<strong>velby!</strong></span>
      </div>
    </div>

    <div class="hero-visual" role="img" aria-label="Fanned stack of printed flyers, brochures, folded leaflets and business cards"></div>
  </section>

  <section class="categories">
    <h2 class="categories-title">Choose By Popular Categories</h2>
    <div class="category-grid">
      <div class="category-card card-banner" role="img" aria-label="Pull-up banner stand on a red background"><h3>Banner<br>&amp; Signage</h3></div>
      <div class="category-card card-brochures" role="img" aria-label="Printed spa brochures on a yellow background"><h3>Brochures<br>&amp; Flyers</h3></div>
      <div class="category-card card-business" role="img" aria-label="Stack of business cards on an orange background"><h3>Business<br>Cards</h3></div>
      <div class="category-card card-labels" role="img" aria-label="Sheets of round stickers on blue wooden boards"><h3>Labels &amp;<br>Stickers</h3></div>
    </div>
  </section>
</div>
</body>
</html>
```